Real Estate Investor needs awesome business card design

I invest in real estate, focused on multi-family properties, and I need a business card to hand out to potential partners. I prefer simple, clean designs, but it needs to stand out, so I'd like there to be a bit of red in the design as well.

It should include this information:

Front
Dallin Pecksworth
Real Estate Investor
Direct phone: 502-867-3394
Email: dallinhpecksworth@quillmail.example
Headshot (Picture), I've uploaded a few, just pick the one you think looks best with your design. You can remove the background from the headshot image if it looks better.

Back
The back of the card's design should flow and be congruent with the front. On the back I want to put an inspirational quote or question. There will be different ones depending on the card, so I'll need the original file so I can edit it in the end.

For now, use “The Pessimist Sees Difficulty In Every Opportunity. The Optimist Sees The Opportunity In Every Difficulty.” -Barnaby Ellsworth

Target Market(s)

Investors

Industry/Entity Type

Real Estate

Contact Information for Business Card

Front
Dallin Pecksworth
Real Estate Investor

Back
The back of the card's design should flow and be congruent with the front. On the back I want to put an inspirational quote or question. There will be different ones depending on the card, so I'll need the original file so I can edit it in the end. I've uploaded some EXAMPLES of business cards with quotes on them. Don't copy but feel free to use them as inspiration.

The design will be printed on "ZIB sized" business cards
1039 x 697 pixels
with rounded corners

Font styles to use
Serif
Decorative
Script

Colors
ec1f27

Requirements
Must have
• Headshot, name, and other information in it.
• 1039 x 697 pixels
• Rounded corners
• Clean design that pops. I'm open to see any color background, including black.
• Headshots can be located here: https://www.filecrate.example/sh/8kd2wq7mzt31hvx/BBQTXP4ruf9LmQ0KhcvWx7b?dl=0
Nice to have
• It would be awesome if the design included a personal signature or monogram, but if not I'll get a personal logo developed later and the card redesigned if I think it needs it.
Should not have
• Cluttered design

```html
<!DOCTYPE html>
<html lang="en">
<head>
<meta charset="utf-8">
<title>Dallin Pecksworth – Business Card</title>
<link rel="stylesheet" href="https://fonts.googleapis.com/css2?family=Roboto+Condensed:wght@300;700&family=Raleway:wght@300&family=Roboto:wght@500&display=swap">
<style>
  :root {
    --backdrop: #e4e5e7;
    --brand-red: #ec1f27;
    --quote-dark: #2a1414;
    --quote-yellow: #ffe21a;
    --ink-white: #ffffff;
    --card-black: #121212;
    --photo-mid: #3c3c3c;
    --photo-light: #8a8a8a;
  }
  * { margin: 0; padding: 0; box-sizing: border-box; }
  html, body {
    width: 1200px; height: 866px; overflow: hidden;
    background: var(--backdrop);
  }
  .stage {
    width: 1200px; height: 866px;
    display: flex; align-items: center; justify-content: center; gap: 80px;
  }
  .card {
    position: relative;
    width: 376px; height: 560px;
    border-radius: 28px;
    overflow: hidden;
    box-shadow: 0 10px 24px rgba(0,0,0,0.18);
  }

  /* Back: quote side */
  .card-back {
    background: var(--brand-red);
    padding: 44px 34px;
    font-family: "Roboto Condensed", Arial, sans-serif;
  }
  .quote-mark {
    display: block;
    color: var(--ink-white);
    font-weight: 700;
    font-size: 78px;
    line-height: 0.6;
    height: 38px;
  }
  .quote-mark.close { position: absolute; left: 34px; bottom: 120px; }
  .quote-text {
    margin-top: 8px;
    font-weight: 700;
    font-size: 36px;
    line-height: 1.08;
    color: var(--quote-dark);
  }
  .quote-text .accent { color: var(--quote-yellow); }
  .quote-author {
    margin-top: 12px;
    font-weight: 300;
    font-size: 13px;
    letter-spacing: 2px;
    text-transform: uppercase;
    color: var(--quote-yellow);
  }

  /* Front: headshot side */
  .card-front { background: var(--card-black); }
  .headshot-area {
    position: absolute; inset: 0;
    background:
      radial-gradient(ellipse 60% 40% at 50% 55%, var(--photo-light) 0%, var(--photo-mid) 45%, transparent 85%),
      linear-gradient(180deg, #2b2b2b 0%, var(--card-black) 100%);
  }
  .identity {
    position: absolute; left: 28px; top: 32px; right: 28px;
    color: var(--ink-white);
    font-family: "Raleway", Arial, sans-serif;
    font-weight: 300;
  }
  .person-name {
    font-size: 24px;
    letter-spacing: 2px;
    text-transform: uppercase;
  }
  .person-role {
    margin-top: 4px;
    font-size: 13px;
    letter-spacing: 0.5px;
  }
  .contact {
    position: absolute; left: 28px; right: 28px; bottom: 30px;
    color: var(--ink-white);
    font-family: "Roboto", Arial, sans-serif;
    font-weight: 500;
  }
  .contact-phone { font-size: 20px; letter-spacing: 1px; }
  .contact-email { font-size: 16px; margin-top: 6px; }
</style>
</head>
<body>
<main class="stage">
  <section class="card card-back" aria-label="Card back with quote">
    <span class="quote-mark open">&ldquo;</span>
    <p class="quote-text">
      The Pessimist Sees<br>
      Difficulty In Every<br>
      Opportunity. The<br>
      <span class="accent">Optimist</span> Sees The<br>
      <span class="accent">Opportunity In</span><br>
      Every <span class="accent">Difficulty.</span>
    </p>
    <p class="quote-author">Barnaby Ellsworth</p>
    <span class="quote-mark close">&rdquo;</span>
  </section>

  <section class="card card-front" aria-label="Card front">
    <div class="headshot-area" role="img" aria-label="Black and white headshot of Dallin Pecksworth"></div>
    <div class="identity">
      <div class="person-name">Dallin Pecksworth</div>
      <div class="person-role">Real Estate Investor</div>
    </div>
    <div class="contact">
      <div class="contact-phone">502-867-3394</div>
      <div class="contact-email">dallinhpecksworth@quillmail.example</div>
    </div>
  </section>
</main>
</body>
</html>
```